If everything digital fails, here's what to do

Hi, I would like a poster / infographic of a list of practical actions people could take in case the internet stops working. I've put together a list of 8 areas, with the situation for each, and the mitigation actions folks can take - I need it presented in a clear and aesthetically pleasing way. I will send you the file with the full text so you can include it all

Target Market(s)

General population, but likely people who are safety conscious and want to protect themselves and learn more about what to do to be tech literate and prepared

Industry/Entity Type

Tech / Cyber / Public safety / Civic tech

Font styles to use
Sans Serif

Requirements
Must have
• It's a lot of text, so I think the important thing is to have it all in one poster, or in a series of similar pages
Nice to have
• I would like it to be a bit brooding, but also elicit competence and that some experts have thought about this and it will all be okay
Should not have
• I don't want it to look cartoonish, or cheap - less is more is sort of what I'm looking for

```html
<!DOCTYPE html>
<html lang="en">
<head>
<meta charset="utf-8">
<title>If Everything Digital Fails – Here's What To Do</title>
<link rel="stylesheet" href="https://fonts.googleapis.com/css2?family=Russo+One&family=Roboto+Condensed:wght@400;700;900&display=swap">
<style>
  :root{
    --stage:#474747;
    --paper:#ececec;
    --ink:#2b2b2b;
    --ink-soft:#555;
    --pink:#ee3d8f;
    --comms:#1f7fb6;
    --transport:#27b3d8;
    --bank-store:#7b2a80;
    --bank-online:#e2197f;
    --info-pass:#f5822a;
    --info-cloud:#f4c12a;
    --tech-devices:#6cc39b;
    --tech-home:#1d9a58;
  }
  *{box-sizing:border-box;margin:0;padding:0}
  html,body{width:1200px;height:1200px;overflow:hidden;background:var(--stage)}
  body{position:relative;font-family:"Roboto Condensed",Arial,sans-serif;color:var(--ink)}

  .poster{position:absolute;left:0;top:178px;width:1200px;height:844px;overflow:hidden;
    background:radial-gradient(ellipse at 50% 35%,#fafafa 0%,#e6e6e6 55%,#cfcfcf 100%)}

  .hero{position:absolute;left:320px;top:20px;width:562px;text-align:center}
  .hero__line{font-family:"Russo One",Arial,sans-serif;font-size:34px;letter-spacing:3px;color:#4a4a4a;line-height:1.15}
  .hero__band{margin:8px -30px;height:62px;display:flex;align-items:center;justify-content:center;
    background:linear-gradient(90deg,rgba(238,61,143,0) 0%,var(--pink) 22%,var(--pink) 78%,rgba(238,61,143,0) 100%)}
  .hero__fails{font-family:"Russo One",Arial,sans-serif;font-size:54px;letter-spacing:8px;color:var(--pink);
    -webkit-text-stroke:2px #fff;line-height:1}
  .chain-photo{position:absolute;left:320px;top:178px;width:562px;height:160px;
    background:radial-gradient(ellipse at 60% 45%,#f5f5f5 0%,#a9a9a9 45%,#6f6f6f 75%,#d4d4d4 100%)}

  .card{position:absolute;width:268px;display:flex;flex-direction:column}
  .card__head{background:var(--c);color:#fff;display:flex;align-items:center;gap:10px;padding:8px 12px;min-height:64px;border-radius:4px 4px 0 0}
  .card__icon{flex:0 0 34px;height:34px}
  .card__title{font-family:"Russo One",Arial,sans-serif;font-size:15px;letter-spacing:1px;line-height:1}
  .card__sub{font-size:10.5px;line-height:1.2;margin-top:3px}
  .card__label{text-align:center;font-weight:700;font-size:9.5px;letter-spacing:1px;color:var(--c);padding:5px 0 4px;background:#fff}
  .card__body{flex:1;background:#fff;border:1.6px solid var(--c);border-radius:10px;padding:10px 12px;font-size:10px;line-height:1.27;margin:0 6px 6px}
  .card__body p{margin-bottom:6px}
  .card__body strong{font-weight:700}
  .card__frame{background:#fff;flex:1;display:flex;flex-direction:column}

  .refresh{color:var(--c);font-weight:700;text-decoration:underline}
  .step{display:flex;gap:6px;margin-bottom:8px}
  .step__num{font-family:"Russo One",Arial,sans-serif;font-size:20px;color:var(--c);line-height:1;flex:0 0 14px}
  .step__text strong{display:block}

  .comms{--c:var(--comms);left:26px;top:26px;height:534px}
  .transport{--c:var(--transport);left:26px;top:583px;height:240px}
  .bank-store{--c:var(--bank-store);left:320px;top:338px;height:222px}
  .bank-online{--c:var(--bank-online);left:320px;top:583px;height:240px}
  .info-pass{--c:var(--info-pass);left:614px;top:338px;height:222px}
  .info-cloud{--c:var(--info-cloud);left:614px;top:583px;height:240px}
  .tech-devices{--c:var(--tech-devices);left:908px;top:26px;height:534px}
  .tech-home{--c:var(--tech-home);left:908px;top:583px;height:240px}
</style>
</head>
<body>
<main class="poster">

  <header class="hero">
    <h1>
      <span class="hero__line" style="display:block">IF EVERYTHING DIGITAL</span>
      <span class="hero__band"><span class="hero__fails">FAILS</span></span>
      <span class="hero__line" style="display:block">HERE'S WHAT TO DO</span>
    </h1>
  </header>
  <div class="chain-photo" role="img" aria-label="Photograph of a metal chain breaking apart in the middle, grey tones"></div>

  <section class="card comms">
    <div class="card__head">
      <svg class="card__icon" viewBox="0 0 34 34" fill="none" stroke="#fff" stroke-width="2"><rect x="13" y="3" width="14" height="24" rx="2"/><line x1="18" y1="23" x2="22" y2="23"/><path d="M3 24c0-4 8-4 8 0v6H3z"/></svg>
      <div><div class="card__title">COMMUNICATIONS</div><div class="card__sub">Cell phones / land-line phone services have stopped working</div></div>
    </div>
    <div class="card__frame">
      <div class="card__label">POSSIBLE MITIGATIONS</div>
      <div class="card__body">
        <div class="step"><span class="step__num">1</span><div class="step__text"><strong>Buy a two-way hand-held walkie talkie &amp; share the other with close friends.</strong><span class="refresh">Refresh when?</span> Check to ensure your walkie talkie has working batteries every 12 months (and that you know / remember how the walkie talkie itself works)</div></div>
        <div class="step"><span class="step__num">2</span><div class="step__text"><strong>Share a 'third space' safe spot with close contacts in town where you know you could meet in emergency situations if your home was not safe to remain in. Do the same with neighbours and folks who live in your neighbourhood - have a central gathering spot in your hood that you share with others so you can have a convening spot close by.</strong><span class="refresh">Refresh when?</span> Have a quick reminder conversation about this with your close contacts every 12 months to ensure everyone knows that's the plan</div></div>
        <div class="step"><span class="step__num">3</span><div class="step__text"><strong>Have a printed list of your close contacts' home addresses handy, if you don't know how to get to their places by heart.</strong><span class="refresh">Refresh when?</span> Print a new such document every 12 months to ensure it stays up to date</div></div>
        <div class="step"><span class="step__num">4</span><div class="step__text"><strong>Have a list of close contacts that might still have a working landline (ie. rotary, not voip-based), or who have a satellite phone</strong><span class="refresh">Refresh when?</span> Remind yourself of this list and refresh it every 12 months or so</div></div>
        <div class="step"><span class="step__num">5</span><div class="step__text"><strong>Make a list of the people in your life that you care about that may also be affected, and make sure you include individuals in your community that may be vulnerable in such a disruption (they may be older, may live alone, might need access to supply of medication).</strong><span class="refresh">Refresh when?</span> Remind yourself of this list and refresh it every 12 months or so</div></div>
      </div>
    </div>
  </section>

  <section class="card transport">
    <div class="card__head">
      <svg class="card__icon" viewBox="0 0 34 34" fill="#fff"><rect x="6" y="5" width="15" height="25" rx="2"/><rect x="9" y="8" width="9" height="6" fill="var(--transport)"/><path d="M21 12h4l3 4v10a2 2 0 0 1-4 0v-6h-3" fill="none" stroke="#fff" stroke-width="2"/></svg>
      <div><div class="card__title">TRANSPORTATIONS</div><div class="card__sub">Gas stations have stopped working</div></div>
    </div>
    <div class="card__frame">
      <div class="card__label">POSSIBLE MITIGATIONS</div>
      <div class="card__body">
        <p><strong>(If you own a car)<br>Have a standard 40L gas canister filled with gas and available close by in case needed.</strong></p>
        <p><span class="refresh">Refresh when?</span> Use up the gas within 4 months or so, and refill the canister then (i.e. 3 times a year) so that it remains usable</p>
        <p><span class="refresh">Refresh when?</span> (If relevant) ensure the can is not in a place where kids can get to it, since it's not safe for kids to be around gas</p>
      </div>
    </div>
  </section>

  <section class="card bank-store">
    <div class="card__head">
      <svg class="card__icon" viewBox="0 0 34 34" fill="none" stroke="#fff" stroke-width="2"><rect x="3" y="8" width="28" height="19" rx="2"/><line x1="3" y1="14" x2="31" y2="14" stroke-width="3"/><line x1="7" y1="21" x2="15" y2="21"/></svg>
      <div><div class="card__title">BANKING</div><div class="card__sub">Debit and credit cards have stopped working (in stores; ATMs)</div></div>
    </div>
    <div class="card__frame">
      <div class="card__label">POSSIBLE MITIGATIONS</div>
      <div class="card__body">
        <p><strong>Have $500 in cash available in $20 bills.</strong><br><span class="refresh">Refresh when?</span> N/A once done</p>
      </div>
    </div>
  </section>

  <section class="card bank-online">
    <div class="card__head">
      <svg class="card__icon" viewBox="0 0 34 34" fill="#fff"><path d="M17 3 3 10h28z"/><rect x="6" y="12" width="3" height="12"/><rect x="12" y="12" width="3" height="12"/><rect x="19" y="12" width="3" height="12"/><rect x="25" y="12" width="3" height="12"/><rect x="3" y="26" width="28" height="3"/></svg>
      <div><div class="card__title">BANKING</div><div class="card__sub">Debit and credit cards have stopped working; your bank can't access its own information (online)</div></div>
    </div>
    <div class="card__frame">
      <div class="card__label">POSSIBLE MITIGATIONS</div>
      <div class="card__body">
        <p><strong>Print paper records of your banking statements that prove what you have in your bank accounts and store it in a safe place in your living space.</strong> Ensure it has dates showing and full amounts, as well as your identifiers (name and account numbers) as well as the institution itself (printed screenshots should work fine if your money is in a few accounts requiring many statements). Note the same goes for your liabilities (i.e. be able to prove how much you had left on your mortgage or other bigger loans, if you have such debt).</p>
        <p><span class="refresh">Refresh when?</span> Update this document every 6-12 months</p>
      </div>
    </div>
  </section>

  <section class="card info-pass">
    <div class="card__head">
      <svg class="card__icon" viewBox="0 0 34 34" fill="none" stroke="#fff" stroke-width="2.2"><rect x="6" y="15" width="22" height="15" rx="2" fill="#fff"/><path d="M11 15V10a6 6 0 0 1 12 0v5"/><circle cx="17" cy="22" r="2" fill="var(--info-pass)" stroke="none"/></svg>
      <div><div class="card__title">INFORMATION MANAGEMENT</div><div class="card__sub">Password manager services (cloud) have stopped working</div></div>
    </div>
    <div class="card__frame">
      <div class="card__label">POSSIBLE MITIGATIONS</div>
      <div class="card__body">
        <p>Preamble: Many individuals don't remember their passwords anymore, having password managers generate complicated strings of characters as their passwords for their many digital accounts in their lives. <strong>Print a full list of your accounts and their passwords and keep that document safely in your living space.</strong></p>
        <p><span class="refresh">Refresh when?</span> Print a new such document every 6 months to ensure the list remains up to date</p>
      </div>
    </div>
  </section>

  <section class="card info-cloud">
    <div class="card__head">
      <svg class="card__icon" viewBox="0 0 34 34" fill="none" stroke="#fff" stroke-width="2"><path d="M9 22a6 6 0 0 1 1-12 8 8 0 0 1 15 2 5 5 0 0 1 0 10z"/><line x1="17" y1="22" x2="17" y2="30"/><line x1="10" y1="30" x2="24" y2="30"/></svg>
      <div><div class="card__title">INFORMATION MANAGEMENT</div><div class="card__sub">Cloud storage services have stopped working</div></div>
    </div>
    <div class="card__frame">
      <div class="card__label">POSSIBLE MITIGATIONS</div>
      <div class="card__body">
        <p><strong>Do a backup of the important documents that are stored only in your cloud storage (e.g. that important email in your PostBox Mail; that tax document only issued digitally, etc.)</strong><br><span class="refresh">Refresh when?</span> Do a backup and update every 6 months<br>Note: Since this is a time-consuming exercise but not necessarily the same exercise as #7 below, you could alternate the months when you do one versus the other. For example, you could do this with annual equinoxes: March 21 and Sept 21 (pro tip: star email messages that are important as they arrive, so that you know what needs to be backed up every six months; that way, you don't have to go searching through your whole inbox)</p>
      </div>
    </div>
  </section>

  <section class="card tech-devices">
    <div class="card__head">
      <svg class="card__icon" viewBox="0 0 34 34" fill="none" stroke="#fff" stroke-width="2"><rect x="3" y="5" width="22" height="15" rx="1"/><line x1="10" y1="25" x2="18" y2="25"/><rect x="22" y="13" width="9" height="15" rx="1" fill="var(--tech-devices)"/></svg>
      <div><div class="card__title">TEHNOLOGY</div><div class="card__sub">Computers (laptops, tablets, smart phones) have stopped working</div></div>
    </div>
    <div class="card__frame">
      <div class="card__label">POSSIBLE MITIGATIONS</div>
      <div class="card__body">
        <div class="step"><span class="step__num">1</span><div class="step__text"><strong>Save all important digital materials (e.g. photos) that don't also exist on paper on a portable hard drive. Remember to do this for all digital materials that have been saved to your cloud that you might have forgotten about (archived, etc.).</strong><span class="refresh">Refresh when?</span> Do a backup and update every 6 months<br>Note: Since this is time-consuming, put a note in your calendar at the beginning of the year, choosing the time and date when you will do this (as noted in #5 above, you could do this in line with the solstice each year: June 20 and December 20)</div></div>
        <div class="step"><span class="step__num">2</span><div class="step__text"><strong>Get a hand cranked radio to ensure you have access to important news and information about what's happening in your community (locally, as well as nationally/internationally).</strong><span class="refresh">Refresh when?</span> Make sure the hand cranked radio has fresh batteries (change them every 12 months or so)</div></div>
        <div class="step"><span class="step__num">3</span><div class="step__text"><strong>Download a copy of your city's maps (e.g. MapWays) on your phone for local access, and make sure you have a physical map in case you need to get somewhere new in your city in a rush, and you don't know how to get there.</strong><span class="refresh">Refresh when?</span> N/A once done</div></div>
      </div>
    </div>
  </section>

  <section class="card tech-home">
    <div class="card__head">
      <svg class="card__icon" viewBox="0 0 34 34" fill="none" stroke="#fff" stroke-width="2.2"><path d="M4 16 17 5l13 11"/><path d="M8 14v15h18V14"/><path d="M12 21a7 7 0 0 1 10 0"/><circle cx="17" cy="25" r="1.5" fill="#fff"/></svg>
      <div><div class="card__title">TEHNOLOGY</div><div class="card__sub">Smart home devices have stopped working</div></div>
    </div>
    <div class="card__frame">
      <div class="card__label">POSSIBLE MITIGATIONS</div>
      <div class="card__body">
        <p><strong>If you have a smart home device that needs to be connected to the internet to work and that doesn't have a manual override (e.g. a smart lock for your living space's main door, or for the garage) ensure you have a backup system in place that would not leave you stranded when the internet goes down.</strong></p>
        <p><span class="refresh">Refresh when:</span> N/A once done</p>
      </div>
    </div>
  </section>

</main>
</body>
</html>
```